We are looking for a clean new looking business card.

We would like a new, clean, and modern type business card with our updated contact information. We are a small a plumbing and heating and gasfitting company who offer 24 hr emergency service as well.
We feel our logo looks best on a white background.
Our current cards are outdated, both the design and the information.

Industry/Entity Type

Plumbing and heating

Contact Information for Business Card

Logo, Name, Title, Phone#, Email, Website, "24/7 Emergency Service"

Colors
0054AA
0677BA
7BADD7
CADEEF
E8F1F8

```html
<!DOCTYPE html>
<html lang="en">
<head>
<meta charset="UTF-8">
<title>Harbourline Business Card</title>
<link rel="stylesheet" href="https://fonts.googleapis.com/css2?family=Montserrat:wght@400;500;600;700;800&display=swap">
<style>
  :root {
    --navy: #0054AA;
    --blue: #0677BA;
    --sky: #7BADD7;
    --mist: #CADEEF;
    --ice: #E8F1F8;
    --ink: #2b2b2b;
    --grey: #555b61;
    --paper: #ffffff;
    --stage: #1f1f21;
  }
  * { margin: 0; padding: 0; box-sizing: border-box; }
  html, body { width: 1200px; height: 800px; overflow: hidden; }
  body {
    background: var(--stage);
    font-family: "Montserrat", Arial, sans-serif;
    display: flex;
    align-items: center;
    justify-content: center;
    gap: 40px;
  }
  .card {
    position: relative;
    width: 540px;
    height: 309px;
    background: var(--paper);
    border-radius: 18px;
    overflow: hidden;
  }

  /* Brand lockup */
  .brand { display: flex; flex-direction: column; align-items: flex-start; }
  .brand-row { display: flex; align-items: center; gap: 8px; }
  .brand-dot { border-radius: 50%; background: var(--blue); flex: none; }
  .brand-name { font-weight: 800; color: var(--blue); letter-spacing: 0.5px; line-height: 1; white-space: nowrap; }
  .brand-tagline { font-weight: 600; color: var(--ink); text-transform: uppercase; white-space: nowrap; }

  /* Front */
  .card-front .brand { position: absolute; left: 32px; top: 110px; width: 206px; }
  .card-front .brand-dot { width: 18px; height: 18px; }
  .card-front .brand-name { font-size: 24px; }
  .card-front .brand-tagline { font-size: 7px; letter-spacing: 1.9px; margin-top: 8px; }

  .divider {
    position: absolute; left: 258px; top: 72px;
    width: 1px; height: 118px; background: var(--ink);
  }
  .contact { position: absolute; left: 280px; top: 64px; }
  .contact-name { font-size: 20px; font-weight: 700; color: var(--ink); text-transform: uppercase; letter-spacing: 0.3px; }
  .contact-title { font-size: 13px; font-weight: 500; color: var(--blue); margin: 2px 0 12px; }
  .contact-list { list-style: none; }
  .contact-list li {
    display: flex; align-items: center; gap: 9px;
    font-size: 11px; color: var(--grey); margin-bottom: 6px;
  }
  .contact-list svg { width: 11px; height: 11px; flex: none; }

  .emergency {
    position: absolute; left: 280px; top: 214px;
    font-size: 13px; font-weight: 500; color: var(--ink); text-transform: uppercase;
  }
  .emergency span { color: var(--blue); font-weight: 600; }

  .edge-band {
    position: absolute; left: 0; right: 0; bottom: 0; height: 12px;
    display: flex; gap: 3px; background: var(--paper);
  }
  .edge-band i { flex: 1; }
  .edge-band i:nth-child(1) { background: var(--navy); }
  .edge-band i:nth-child(2) { background: var(--blue); }
  .edge-band i:nth-child(3) { background: #3e93c9; }
  .edge-band i:nth-child(4) { background: var(--sky); }
  .edge-band i:nth-child(5) { background: var(--mist); }

  /* Back */
  .card-back { display: flex; align-items: center; justify-content: center; }
  .card-back .brand { align-items: center; }
  .card-back .brand-row { gap: 14px; }
  .card-back .brand-dot { width: 40px; height: 40px; }
  .card-back .brand-name { font-size: 54px; }
  .card-back .brand-tagline { font-size: 13px; letter-spacing: 4px; margin-top: 14px; }
</style>
</head>
<body>

  <section class="card card-front">
    <div class="brand">
      <div class="brand-row">
        <span class="brand-dot"></span>
        <span class="brand-name">Harbourline</span>
      </div>
      <span class="brand-tagline">Plumbing · Heating · Gasfitting</span>
    </div>

    <div class="divider"></div>

    <div class="contact">
      <h1 class="contact-name">Daniel Reeve</h1>
      <p class="contact-title">Founder &amp; CEO</p>
      <ul class="contact-list">
        <li>
          <svg viewBox="0 0 12 12" aria-hidden="true"><circle cx="6" cy="6" r="6" fill="var(--blue)"/><path d="M4 3.2l1 1.2-.6.7c.4.8 1 1.4 1.8 1.8l.7-.6 1.2 1-.6.9C5.6 8.1 3.9 6.4 3.3 4z" fill="#fff"/></svg>
          (555) 014-2288
        </li>
        <li>
          <svg viewBox="0 0 12 12" aria-hidden="true"><rect x="1" y="2.5" width="10" height="7" rx="1" fill="var(--blue)"/><path d="M1.5 3l4.5 3.5L10.5 3" stroke="#fff" stroke-width="1" fill="none"/></svg>
          daniel@harbourline.com
        </li>
        <li>
          <svg viewBox="0 0 12 12" aria-hidden="true"><circle cx="6" cy="6" r="5.5" fill="var(--blue)"/><ellipse cx="6" cy="6" rx="2.3" ry="5" stroke="#fff" stroke-width=".8" fill="none"/><path d="M1 6h10" stroke="#fff" stroke-width=".8"/></svg>
          www.harbourline.com
        </li>
      </ul>
    </div>

    <p class="emergency"><span>24/7</span> Emergency Service</p>

    <div class="edge-band"><i></i><i></i><i></i><i></i><i></i></div>
  </section>

  <section class="card card-back">
    <div class="brand">
      <div class="brand-row">
        <span class="brand-dot"></span>
        <span class="brand-name">Harbourline</span>
      </div>
      <span class="brand-tagline">Plumbing · Heating · Gasfitting</span>
    </div>
  </section>

</body>
</html>
```